Joomla Responsive Website Template for an International Biotechnology Company

Our client is a biotechnology company that uses silver-based technology to help make products antimicrobial, antibacterial, and anti fungal. We need a Joomla-based template that is responsive/mobile friendly when viewed on tablets or smartphones. We are looking for a template design for the home page and subpages. We are replacing the current website http://www.velmora-labs.com with a new website being built here: http://velmoraclean.com.stagehost.com/velmoraprime/. What we have now on the site is the basic wire frame. This is the desired layout and pictures we want to use. We would like you to add some design elements to make the website more professional looking and polished. Please refer to the attached style guide to help you in choosing the color. The client does like the green leaf, which is included in the last page of style guide and may be good for a background image. While the Velmora logo and leaf are green, we do not want to overuse the color green. The client does own other technologies that we will be promoting on the site and the logos for these technologies are attached below. These logos are Tusk, Velmora-Prime, and Pivn. We will be using this website to promote the technologies, the markets the technologies serve; drinking water, medical devices, apparel and textiles, and architectural surfaces, and to promote the customer using these devices. Please make the design "clean" and not cluttered, as these technologies are used to fight "dirty things".
Updates

Hello Designers! Thank you all very much for your design submissions. They were simply excellent. Due to the Holidays and New Years, many of the client's team members have been on vacation. We expect to have feedback shortly and pick the top design soon there after. Again, thank you all very much and hope the New Year brings you continued success. Best, Dorian

Industry/Entity Type

Biotechnology

Coding

Coded - Design and coding required

```html
<!DOCTYPE html>
<html lang="en">
<head>
<meta charset="utf-8">
<title>Velmora – Keeping the world's surfaces safe</title>
<link href="https://fonts.googleapis.com/css2?family=Open+Sans:wght@400;600;700&display=swap" rel="stylesheet">
<style>
:root{
  --green:#7ab929;
  --green-bright:#7dc242;
  --ink:#3f3f3f;
  --body:#555;
  --muted:#9a9a9a;
  --rule:#dcdcdc;
  --band:#f2f2f2;
  --white:#fff;
}
*{box-sizing:border-box;margin:0;padding:0}
html,body{width:758px;height:1200px;overflow:hidden;background:var(--white)}
body{position:relative;font-family:"Open Sans",Arial,sans-serif;color:var(--ink)}
.abs{position:absolute}

/* hero */
.hero{left:0;top:0;width:758px;height:324px;
  background:linear-gradient(160deg,#eef4fb 0%,#cfe0f2 45%,#9ec0e6 75%,#7aa6d8 100%)}
.hero-arrow{top:127px;width:28px;height:50px}
.hero-arrow.prev{left:48px}
.hero-arrow.next{left:694px}
.hero-card{left:325px;top:88px;width:311px;height:139px;background:rgba(235,240,246,.78)}
.hero-card .kicker{position:absolute;left:24px;top:18px;font-size:18px;color:#333}
.hero-card .headline{position:absolute;left:24px;top:38px;font-size:36px;font-weight:700;color:var(--green)}
.hero-card .sub{position:absolute;left:22px;top:88px;font-size:17.5px;color:#222}

/* header */
.lang{left:615px;top:325px;width:66px;height:16px;border:1px solid var(--rule);border-top:none;font-size:7.5px;color:#666;display:flex;align-items:center;gap:4px;padding-left:5px;background:var(--white)}
.lang .flag{width:9px;height:6px;background:#2b4a9b}
.brand{left:75px;top:343px;height:36px;display:flex;align-items:center;gap:7px;font-size:28px;font-weight:600;color:var(--green)}
.brand .mark{width:12px;height:12px;background:var(--green)}
.search{left:366px;top:348px;width:140px;height:20px;border:1px solid var(--rule);font-size:9.5px;color:#444;padding:3px 8px}
.search svg{position:absolute;right:6px;top:3px}
.social{top:348px;width:20px;height:20px;border-radius:3px;display:flex;align-items:center;justify-content:center;font-size:5.5px;font-weight:600;color:var(--white)}
.social.loopa{left:519px;background:#2aa0db}
.social.circlo{left:541px;background:#3b5998}
.tech{top:348px;height:20px;border:1px solid var(--rule);border-radius:3px;display:flex;align-items:center;justify-content:center;font-size:9px;font-weight:700;color:var(--ink)}
.tech.prime{left:569px;width:37px}
.tech.pivn{left:610px;width:30px}
.tech.tusk{left:645px;width:36px}
.nav{left:0;top:392px;width:758px;height:19px;border-bottom:2px solid var(--green-bright)}
.nav a{position:absolute;top:2px;font-size:9.6px;color:#777;text-decoration:none}
.nav a.active{top:1px;height:16px;padding:1px 6px;background:var(--green-bright);color:var(--white)}

/* markets */
.section-title{font-size:18px;font-weight:600;color:var(--ink)}
.markets-title{left:0;width:758px;top:441px;text-align:center}
.market{top:484px;width:141px}
.market h3{font-size:9.5px;font-weight:600;text-align:center;color:var(--ink);height:20px}
.market .photo{width:141px;height:131px;border:1px solid #ccc}
.market p{font-size:7px;line-height:9px;color:#333;margin-top:3px}
.market a{display:block;font-size:7px;line-height:10px;color:var(--green);text-decoration:underline}

/* about band */
.band{left:0;top:692px;width:758px;height:164px;background:var(--band)}
.leaf{left:520px;top:692px;width:238px;height:150px;
  background:radial-gradient(ellipse 60% 45% at 65% 50%,#9ed05a 0%,#76b43a 45%,rgba(118,180,58,0) 75%)}
.about-title{left:75px;top:706px;font-size:20px}
.about-title sup{font-size:11px}
.about-copy{left:75px;top:738px;width:430px;font-size:8.9px;line-height:16.4px;color:var(--body)}

/* news & partners */
.news-title{left:75px;top:876px;font-size:16px}
.news-item{left:75px;width:230px;font-size:7.8px;line-height:12px;font-weight:700;color:#333}
.news-link{color:var(--green);text-decoration:underline}
.news-item time{display:block;font-weight:400;color:var(--muted)}
.partners-title{left:401px;top:876px;font-size:16px}
.partners-copy{left:401px;top:907px;width:285px;font-size:9.4px;line-height:14.6px;color:var(--body)}
.signature{left:583px;top:1019px;font-size:9.8px;line-height:10px;color:#333}
.signature strong{font-weight:600;display:block}

/* partner strip */
.partner{top:1102px;height:24px;display:flex;align-items:center;justify-content:center;font-size:13px;font-weight:700;color:#2d3a55}

/* footer */
.footer-rule{left:75px;top:1156px;width:610px;height:2px;background:var(--green-bright)}
.footer-brand{left:80px;top:1165px;height:18px;display:flex;align-items:center;gap:4px;font-size:13px;font-weight:600;color:var(--green)}
.footer-brand .mark{width:6px;height:6px;background:var(--green)}
.footer-nav a{position:absolute;top:1168px;font-size:8px;color:#777;text-decoration:none}
</style>
</head>
<body>

<section class="abs hero" role="img" aria-label="Photograph of a pipette releasing a blue drop over glass test tubes"></section>
<svg class="abs hero-arrow prev" viewBox="0 0 28 50"><polyline points="26,2 3,25 26,48" fill="none" stroke="rgba(255,255,255,.8)" stroke-width="2"/></svg>
<svg class="abs hero-arrow next" viewBox="0 0 28 50"><polyline points="2,2 25,25 2,48" fill="none" stroke="rgba(255,255,255,.8)" stroke-width="2"/></svg>
<div class="abs hero-card">
  <p class="kicker">Keeping the world’s</p>
  <p class="headline">Surfaces Safe</p>
  <p class="sub">consumer, healthcare, industrial</p>
</div>

<header>
  <div class="abs lang"><span class="flag"></span>English
    <svg width="7" height="5" viewBox="0 0 7 5" style="margin-left:6px"><polyline points="1,1 3.5,3.5 6,1" fill="none" stroke="#444" stroke-width="1.2"/></svg>
  </div>
  <div class="abs brand"><span class="mark"></span>Velmora</div>
  <div class="abs search">Search ...
    <svg width="14" height="13" viewBox="0 0 14 13"><circle cx="5" cy="5" r="3.8" fill="none" stroke="#888" stroke-width="1.4"/><line x1="8" y1="8" x2="13" y2="12" stroke="#888" stroke-width="2"/></svg>
  </div>
  <div class="abs social loopa">Loopa</div>
  <div class="abs social circlo">Circlo</div>
  <div class="abs tech prime">Prime</div>
  <div class="abs tech pivn">Pivn</div>
  <div class="abs tech tusk">Tusk</div>
  <nav class="abs nav">
    <a style="left:81px">Home</a>
    <a style="left:147px">About Us</a>
    <a style="left:227px">Markets</a>
    <a class="active" style="left:296px">Technology</a>
    <a style="left:391px">Customer Programs</a>
    <a style="left:516px">News Highlights</a>
    <a style="left:625px">Contact Us</a>
  </nav>
</header>

<main>
  <h2 class="abs section-title markets-title">Our Markets</h2>

  <article class="abs market" style="left:76px">
    <h3>Drinking Water</h3>
    <div class="photo" role="img" aria-label="Photo of a water filter pitcher" style="background:linear-gradient(180deg,#2c4f86,#122a52)"></div>
    <p>Lorem ipsum dolor sit amet, consec sit tetur adipiscing elit sed do.</p>
    <a>Learn More</a>
  </article>
  <article class="abs market" style="left:230px">
    <h3>Medical Devices</h3>
    <div class="photo" role="img" aria-label="Photo of a nurse at a hospital bedside monitor" style="background:linear-gradient(180deg,#c9d4dc,#8fa8bf)"></div>
    <p>Lorem ipsum dolor sit amet, consec sit tetur adipiscing elit sed do.</p>
    <a>Learn More</a>
  </article>
  <article class="abs market" style="left:385px">
    <h3>Apparel &amp; Textiles</h3>
    <div class="photo" role="img" aria-label="Photo of stacked folded fabrics in grey and blue" style="background:linear-gradient(180deg,#5e6166 0%,#3b3e44 40%,#2e5a95 70%,#6288b6 100%)"></div>
    <p>Lorem ipsum dolor sit amet, consec sit tetur adipiscing elit sed do.</p>
    <a>Learn More</a>
  </article>
  <article class="abs market" style="left:541px">
    <h3>Architectural Surfaces</h3>
    <div class="photo" role="img" aria-label="Photo of a clean laboratory bench with equipment" style="background:linear-gradient(180deg,#e6e9ec,#c4c9ce)"></div>
    <p>Lorem ipsum dolor sit amet, consec sit tetur adipiscing elit sed do.</p>
    <a>Learn More</a>
  </article>

  <section>
    <div class="abs band"></div>
    <div class="abs leaf" role="img" aria-label="Close-up photo of a fresh green leaf"></div>
    <h2 class="abs section-title about-title">Velmora<sup>®</sup> Antimicrobial</h2>
    <p class="abs about-copy">Velmora branded antimicrobial technology makes products cleaner and longer lasting with silver, copper and zinc, which have been proven in use throughout history. Velmora antimicrobial technology provides built-in protection by working 24/7 resisting the growth of microbes. We work in close partnership with our customers, from development to end-user marketing, to deliver a product advantage that makes a real difference in the marketplace. *Velmora is an EPA registered ionic silver technology and is not a nanosilver technology.</p>
  </section>

  <section>
    <h2 class="abs section-title news-title">News &amp; Events</h2>
    <p class="abs news-item" style="top:907px">New Society of Clinical Hygiene of America (SCHA) Guidelines Include Velmora Antimicrobial-Treated Catheters<time>Friday, 12 January 2015</time></p>
    <p class="abs news-item" style="top:967px"><span class="news-link">Harborview Marathon Winner Wears Strideway Shoes Protected by Velmora Antimicrobial</span><time>Saturday, 18 November 2014</time></p>
    <p class="abs news-item" style="top:1015px">Velmora Antimicrobial Incorporated into Tolvane’s Industrial Flooring for Enhanced Microbial Resistance<time>Monday, 10 November 2014</time></p>
  </section>

  <section>
    <h2 class="abs section-title partners-title">Featured Partners</h2>
    <p class="abs partners-copy">Contrary to popular belief, Lorem Ipsum is not simply random text. It has roots in a piece of classical Latin literature from 45 BC, making it over 2000 years old. Edwin Harrow, a Latin professor at Ashgrove College in Virginia, looked up one of the more obscure Latin words, consectetur, from a Lorem Ipsum passage, and going through the cites of the word in classical literature, discovered the undoubtable source.</p>
    <p class="abs signature"><strong>John Doe Smith</strong>CEO, Mc Dowald</p>
  </section>

  <div class="abs partner" style="left:76px;width:92px">Medorvia</div>
  <div class="abs partner" style="left:195px;width:89px">Aquessa</div>
  <div class="abs partner" style="left:300px;width:90px">Purivel</div>
  <div class="abs partner" style="left:405px;width:65px">Cavendra</div>
  <div class="abs partner" style="left:492px;width:98px">Vitrelo</div>
  <div class="abs partner" style="left:612px;width:70px">Galvoro</div>
</main>

<footer>
  <div class="abs footer-rule"></div>
  <div class="abs footer-brand"><span class="mark"></span>Velmora</div>
  <nav class="footer-nav">
    <a style="left:256px">Home</a>
    <a style="left:299px">About Us</a>
    <a style="left:354px">Markets</a>
    <a style="left:403px">Technology</a>
    <a style="left:468px">Customer Programs</a>
    <a style="left:561px">News Highlights</a>
    <a style="left:642px">Contact Us</a>
  </nav>
</footer>

</body>
</html>
```